Architectural, Engineering and Design Build

Tovantek4.com
Veteran Disabled Certified company is doing business in Architecture, Engineer and Design build - look simialr websites and come up with design follow following website
https://harlow-vessant.example/
https://www.quenforgroup.example/
https://www.ddelbmx.example/contract-vehicles/service-disabled-veteran-owned-small-business-sdvosb/
https://www.ostrelgrouplink.example/about/sdvosb/

Target Market(s)

US - Defense and Federal Government

Industry/Entity Type

Colors
0054AA
0677BA
7BADD7
CADEEF
E8F1F8

Requirements
Must have
• Army, American patriotism , Buildings, construction, architecture, engineering
Nice to have
• I need to attract federal government agencies and Defense

```html
<!DOCTYPE html>
<html lang="en">
<head>
<meta charset="UTF-8">
<title>Tovantek – Architecture, Engineer and Design Services</title>
<link rel="stylesheet" href="https://fonts.googleapis.com/css2?family=Montserrat:wght@400;500;600;700;800&display=swap">
<style>
  :root {
    --blue: #0054AA;
    --blue-mid: #0677BA;
    --blue-soft: #7BADD7;
    --blue-pale: #CADEEF;
    --blue-mist: #E8F1F8;
    --red: #E4262B;
    --ink: #141414;
    --text: #333a44;
    --white: #ffffff;
    --black: #050505;
  }
  * { box-sizing: border-box; margin: 0; padding: 0; }
  html, body { width: 1200px; height: 3880px; overflow: hidden; }
  body { font-family: "Montserrat", sans-serif; color: var(--text); background: var(--white); position: relative; }
  .btn { display: inline-block; background: var(--red); color: var(--white); font-weight: 600; font-size: 18px; padding: 13px 30px; text-decoration: none; }

  /* Header */
  .site-header { height: 80px; display: flex; align-items: center; justify-content: space-between; padding: 0 40px; background: var(--white); }
  .brand { font-size: 40px; font-weight: 800; color: var(--blue); letter-spacing: 1px; }
  .main-nav { display: flex; gap: 72px; margin-left: 120px; }
  .main-nav a { color: var(--ink); text-decoration: none; font-size: 19px; font-weight: 500; }
  .site-header .btn { padding: 11px 24px; font-size: 18px; }

  /* Hero */
  .hero { position: relative; height: 640px; display: flex; flex-direction: column; align-items: center; justify-content: center; text-align: center; }
  .hero-photo { position: absolute; inset: 0; background: radial-gradient(ellipse at 50% 10%, #6e5a42 0%, #3a2e24 45%, #1d1814 100%); }
  .hero-photo::after { content: ""; position: absolute; inset: 0; background: rgba(10,10,10,0.35); }
  .hero-content { position: relative; color: var(--white); margin-top: -40px; }
  .hero-kicker { font-size: 24px; font-weight: 600; margin-bottom: 14px; }
  .hero-title { font-size: 60px; font-weight: 700; line-height: 1.2; margin-bottom: 40px; }

  /* About */
  .about { height: 590px; display: flex; align-items: center; padding: 0 130px; gap: 60px; }
  .about-media { position: relative; width: 420px; height: 350px; flex: none; }
  .about-frame { position: absolute; left: 100px; top: -14px; width: 330px; height: 350px; background: var(--blue); border-radius: 0 30px 0 0; }
  .about-photo { position: absolute; left: 0; top: 0; width: 410px; height: 346px; border-radius: 40px 0 40px 40px; background: linear-gradient(135deg, #b9b1aa 0%, #eeeae6 50%, #8a7f78 100%); }
  .about-text h2 { font-size: 30px; font-weight: 700; color: var(--ink); letter-spacing: 1px; margin-bottom: 22px; }
  .about-text p { font-size: 15px; line-height: 1.45; margin-bottom: 18px; max-width: 470px; }
  .about-text .btn { margin-top: 8px; padding: 11px 28px; }

  /* Services */
  .services { height: 590px; display: flex; }
  .services-panel { width: 612px; background: var(--blue); color: var(--white); padding: 50px 60px; }
  .services-panel h2 { font-size: 30px; font-weight: 700; margin-bottom: 38px; }
  .service { display: flex; gap: 26px; margin-bottom: 30px; }
  .service svg { flex: none; width: 62px; height: 62px; }
  .service h3 { font-size: 19px; font-weight: 700; margin-bottom: 8px; }
  .service p { font-size: 14px; line-height: 1.4; max-width: 360px; }
  .services-panel .btn { margin-top: 14px; padding: 11px 28px; }
  .services-photo { flex: 1; background: linear-gradient(180deg, #9fb2c6 0%, #8c6b55 40%, #7c5a46 60%, #5e7a3e 85%, #4c6634 100%); }

  /* Work */
  .work { height: 670px; text-align: center; padding-top: 72px; }
  .section-title { font-size: 30px; font-weight: 700; color: var(--ink); }
  .work-grid { display: flex; justify-content: center; gap: 64px; margin-top: 70px; }
  .work-card { width: 298px; height: 318px; }
  .work-card.c1 { background: linear-gradient(160deg, #8c5e44 0%, #5c7a3a 60%, #bdb8ae 100%); }
  .work-card.c2 { background: linear-gradient(160deg, #6b4e38 0%, #9a8066 50%, #3c3028 100%); }
  .work-card.c3 { background: linear-gradient(170deg, #b9c7d6 0%, #8a5a46 45%, #d9dade 80%, #b0a89e 100%); }
  .dots { display: flex; justify-content: center; gap: 22px; margin-top: 62px; }
  .dots span { width: 18px; height: 18px; border-radius: 50%; background: var(--blue); }
  .dots span.off { background: var(--white); border: 2px solid var(--blue); }

  /* Stats */
  .stats { height: 220px; background: var(--blue); color: var(--white); display: flex; align-items: center; justify-content: space-around; padding: 0 60px; }
  .stat { display: flex; align-items: center; gap: 22px; }
  .stat svg { width: 86px; height: 86px; }
  .stat strong { display: block; font-size: 82px; font-weight: 700; line-height: 1; }
  .stat span { font-size: 18px; }

  /* Reviews */
  .reviews { position: relative; height: 640px; text-align: center; padding-top: 100px; overflow: hidden; }
  .reviews-flag { position: absolute; left: 0; right: 0; bottom: 0; height: 330px; background: linear-gradient(180deg, rgba(255,255,255,1) 0%, rgba(160,170,200,0.5) 35%, #2c3e6e 65%, #8a2230 100%); }
  .review-row { position: relative; display: flex; justify-content: center; gap: 90px; margin-top: 75px; text-align: left; }
  .review { width: 480px; }
  .reviewer { display: flex; align-items: center; gap: 22px; margin-bottom: 14px; }
  .avatar { width: 66px; height: 66px; border-radius: 50%; background: linear-gradient(180deg, var(--blue-pale), var(--blue-soft)); }
  .reviewer h4 { font-size: 19px; font-weight: 700; color: var(--ink); }
  .stars { color: var(--red); font-size: 20px; letter-spacing: 3px; }
  .review p { font-size: 14px; line-height: 1.45; border-bottom: 1px solid #c8c8c8; padding-bottom: 10px; }

  /* Footer */
  .site-footer { height: 440px; background: var(--black); color: var(--white); padding: 80px 90px 0; position: relative; }
  .footer-cols { display: flex; }
  .footer-brand { width: 490px; flex: none; }
  .footer-brand .brand { color: var(--white); font-size: 40px; }
  .footer-brand p { font-size: 15px; margin-top: 14px; }
  .social { display: flex; gap: 40px; margin-top: 30px; }
  .social span { width: 26px; height: 26px; border: 2px solid var(--blue-mid); border-radius: 50%; }
  .footer-links { width: 280px; flex: none; }
  .footer-contact { width: 300px; flex: none; }
  .footer-cols h5 { font-size: 17px; font-weight: 500; letter-spacing: 1px; margin-bottom: 22px; }
  .footer-links ul { list-style: none; }
  .footer-links li { font-size: 15px; margin-bottom: 26px; padding-left: 10px; }
  .contact-item { display: flex; align-items: center; gap: 18px; margin-bottom: 18px; font-size: 15px; }
  .contact-item span { white-space: nowrap; line-height: 1.35; }
  .contact-item svg { width: 42px; height: 42px; flex: none; }
  .footer-bottom { position: absolute; left: 90px; right: 60px; bottom: 28px; display: flex; justify-content: space-between; font-size: 14px; }
</style>
</head>
<body>

<header class="site-header">
  <div class="brand">TOVANTEK</div>
  <nav class="main-nav">
    <a href="#">Home</a><a href="#">About</a><a href="#">Services</a><a href="#">Projects</a>
  </nav>
  <a class="btn" href="#">Contact Us</a>
</header>

<section class="hero">
  <div class="hero-photo" role="img" aria-label="Interior of a federal building lobby with flags and a domed wooden ceiling"></div>
  <div class="hero-content">
    <p class="hero-kicker">Veteran Disabled Certified company</p>
    <h1 class="hero-title">Architecture, Engineer and<br>Design Services</h1>
    <a class="btn" href="#">Contact Us</a>
  </div>
</section>

<section class="about">
  <div class="about-media">
    <div class="about-frame"></div>
    <div class="about-photo" role="img" aria-label="Hands reviewing architectural plans with a pen"></div>
  </div>
  <div class="about-text">
    <h2>WHO WE ARE</h2>
    <p>We deliver architecture, engineering and design build services to federal and defense agencies, combining mission focus with careful planning, disciplined budgets and dependable delivery on every project.</p>
    <p>Our veteran led team brings field tested leadership to each site, from early concept through final inspection.</p>
    <a class="btn" href="#">Read More</a>
  </div>
</section>

<section class="services">
  <div class="services-panel">
    <h2>OUR SERVICES</h2>
    <div class="service">
      <svg viewBox="0 0 62 62" fill="none" stroke="#fff" stroke-width="2.5"><rect x="6" y="20" width="50" height="36"/><path d="M6 20 L31 6 L56 20"/><path d="M16 30h8M16 40h8M38 30h8M38 40h8M27 56V44h8v12"/></svg>
      <div><h3>Architecture</h3><p>Planning and design of secure, lasting federal facilities built to the mission and site.</p></div>
    </div>
    <div class="service">
      <svg viewBox="0 0 62 62" fill="none" stroke="#fff" stroke-width="2.5"><circle cx="31" cy="31" r="10"/><path d="M31 6v10M31 46v10M6 31h10M46 31h10M13 13l7 7M42 42l7 7M13 49l7-7M42 20l7-7"/></svg>
      <div><h3>Engineering</h3><p>Structural, civil and systems engineering that meets strict code and agency standards.</p></div>
    </div>
    <div class="service">
      <svg viewBox="0 0 62 62" fill="none" stroke="#fff" stroke-width="2.5"><rect x="14" y="10" width="22" height="46"/><rect x="36" y="26" width="14" height="30"/><path d="M20 18h10M20 28h10M20 38h10M41 34h4M41 44h4M6 56h50"/></svg>
      <div><h3>Design Build</h3><p>One team for design and construction, cutting schedule risk and keeping budgets on track.</p></div>
    </div>
    <a class="btn" href="#">View Services</a>
  </div>
  <div class="services-photo" role="img" aria-label="Aerial view of a brick federal building with white columns and flags"></div>
</section>

<section class="work">
  <h2 class="section-title">LATEST WORK</h2>
  <div class="work-grid">
    <div class="work-card c1" role="img" aria-label="Brick building entrance with walkway and landscaping"></div>
    <div class="work-card c2" role="img" aria-label="Lobby interior with flags and a visitor walking"></div>
    <div class="work-card c3" role="img" aria-label="Columned brick building exterior with flagpoles"></div>
  </div>
  <div class="dots"><span></span><span class="off"></span><span></span></div>
</section>

<section class="stats">
  <div class="stat">
    <svg viewBox="0 0 86 86" fill="none" stroke="#fff" stroke-width="3"><circle cx="43" cy="34" r="18"/><path d="M43 24l3 6 6 1-4 4 1 6-6-3-6 3 1-6-4-4 6-1z"/><path d="M32 50l-6 24 10-6 7 10M54 50l6 24-10-6-7 10"/></svg>
    <div><strong>20+</strong><span>Years Experience</span></div>
  </div>
  <div class="stat">
    <svg viewBox="0 0 86 86" fill="none" stroke="#fff" stroke-width="3"><rect x="14" y="24" width="26" height="52"/><rect x="40" y="10" width="30" height="66"/><path d="M20 34h14M20 46h14M20 58h14M47 20h16M47 32h16M47 44h16M47 56h16M8 76h70"/></svg>
    <div><strong>97%</strong><span>Repeat Business</span></div>
  </div>
  <div class="stat">
    <svg viewBox="0 0 86 86" fill="none" stroke="#fff" stroke-width="3"><rect x="14" y="8" width="48" height="64" rx="3"/><path d="M24 24h28M24 34h28M24 44h16"/><circle cx="58" cy="58" r="12"/><path d="M53 68l-3 12 8-4 8 4-3-12"/></svg>
    <div><strong>30+</strong><span>Certifications</span></div>
  </div>
</section>

<section class="reviews">
  <div class="reviews-flag" role="img" aria-label="Waving American flag with stars and stripes"></div>
  <h2 class="section-title" style="position:relative">Client Reviews</h2>
  <div class="review-row">
    <article class="review">
      <div class="reviewer"><div class="avatar" role="img" aria-label="Client portrait"></div><div><h4>Mara Delling</h4><div class="stars">★★★★★</div></div></div>
      <p>The team handled our base facility upgrade with precision. Clear reporting, strong safety and a schedule they kept from start to finish.</p>
    </article>
    <article class="review">
      <div class="reviewer"><div class="avatar" role="img" aria-label="Client portrait"></div><div><h4>Mara Delling</h4><div class="stars">★★★★★</div></div></div>
      <p>Professional, responsive and deeply skilled. Their design build approach saved us months and the finished building serves our staff well.</p>
    </article>
  </div>
</section>

<footer class="site-footer">
  <div class="footer-cols">
    <div class="footer-brand">
      <div class="brand">TOVANTEK</div>
      <p>Architecture, Engineer and Design Services</p>
      <div class="social"><span></span><span></span><span></span></div>
    </div>
    <div class="footer-links">
      <h5>QUICK LINKS</h5>
      <ul><li>Home</li><li>About</li><li>Services</li><li>Projects</li></ul>
    </div>
    <div class="footer-contact">
      <h5>CONTACT INFO</h5>
      <div class="contact-item"><svg viewBox="0 0 42 42"><circle cx="21" cy="21" r="20" fill="#0054AA"/><path d="M15 12l4 0 2 5-3 2c1 3 3 5 6 6l2-3 5 2v4c0 1-1 2-2 2-9 0-16-7-16-16 0-1 1-2 2-2z" fill="#fff"/></svg><span>+1 555 0142</span></div>
      <div class="contact-item"><svg viewBox="0 0 42 42"><circle cx="21" cy="21" r="20" fill="#0054AA"/><rect x="11" y="14" width="20" height="14" fill="none" stroke="#fff" stroke-width="2"/><path d="M11 14l10 8 10-8" fill="none" stroke="#fff" stroke-width="2"/></svg><span>hello@tovantek4.com</span></div>
      <div class="contact-item"><svg viewBox="0 0 42 42"><circle cx="21" cy="21" r="20" fill="#0054AA"/><path d="M21 31s-7-8-7-13a7 7 0 0 1 14 0c0 5-7 13-7 13z" fill="#fff"/><circle cx="21" cy="18" r="2.5" fill="#0054AA"/></svg><span>418 Birch Ln SE, Fairmont<br>United States</span></div>
    </div>
  </div>
  <div class="footer-bottom"><span>© 2024 Tovantek. All Rights Reserved.</span><span>Privacy Policy | Terms and Conditions</span></div>
</footer>

</body>
</html>
```